We need a DL size flyer, double sided, for our lawn mowing and gardening business, Kestrel Greens.

We want to run on the front side, the following promotion:
50% off lawn mowing, applies to first lawn mowed on any regular service,
applies to first 100 callers only, so call now!
Professional lawn mowing at an affordable price.

Logo at the bottom left, with Lawn and Garden Maintenance written just below logo.

On bottom Right contact details;
Tom and Gareth
Ph: 0487650912
Email: kestrelgreens@mailbox-example.com
www.kestrelgreens-example.com.au

Front side positioned horizontally, with a bright and colour full design in the background, with the offer of 50% Off lawn mowing in large letters along the top.

On the rear side, also positioned horizontally, a list of our services, stating;

At Kestrel Greens we specialise in the following services;
Lawn mowing
Edging
Blowing
Hedging
Pruning
Tree Loping
Weeding
Poisoning
Mulching
Fertilising
Rubbish removal
Planting
Lawn care and advice
Turf
And any other garden maintenance job,
No job too big or too small.
(No particular order, whatever fits best)
Also include our contact details,
Kestrel Greens
Ph 0487650912
www.kestrelgreens-example.com.au

Target Market(s)

Home owners, aged between 30-50 years old, moderate socio ecenomic status to more afluent areas.

Industry/Entity Type

Business

Requirements
Must have
• DL size, front and back, full colour.
Nice to have
• The writting stating "Kestrel Greens" in our logo is quite bland, if that could also be amended to make it more appealing, but change the writting design only not the actual logo.

```html
<!DOCTYPE html>
<html lang="en">
<head>
<meta charset="utf-8">
<title>Kestrel Greens – DL Flyer</title>
<link rel="stylesheet" href="https://fonts.googleapis.com/css2?family=Lobster&family=Mulish:wght@700;800&display=swap">
<style>
  :root {
    --page: #ffffff;
    --green-deep: #17b52e;
    --green-mid: #1cc13a;
    --green-light: #8ee63a;
    --green-lime: #a6f03c;
    --ribbon: rgba(74, 200, 40, 0.85);
    --orange: #f5861f;
    --yellow-text: #f4ee2a;
    --white: #ffffff;
    --post: #8fe84a;
    --script: "Lobster", cursive;
    --sans: "Mulish", Arial, sans-serif;
  }
  * { box-sizing: border-box; margin: 0; padding: 0; }
  html, body { width: 1181px; height: 1200px; overflow: hidden; background: var(--page); }
  body { position: relative; }

  .flyer {
    position: absolute;
    left: 131px;
    overflow: hidden;
    box-shadow: 0 18px 40px rgba(0,0,0,0.16);
    border: 1px solid #cfcfcf;
  }
  .flyer--front { top: 103px; width: 923px; height: 435px; }
  .flyer--back  { top: 652px; width: 925px; height: 436px; }

  /* ---------- Front ---------- */
  .offer-panel {
    position: absolute; left: 0; top: 0; width: 313px; height: 100%;
    background: var(--white);
    border-right: 4px solid var(--green-light);
  }
  .offer-headline {
    position: absolute; left: 46px; top: 22px;
    font-family: var(--script);
    color: var(--green-mid);
    transform: rotate(-4deg);
    transform-origin: left top;
    line-height: 1;
    text-align: center;
  }
  .offer-headline .big { display: block; font-size: 66px; }
  .offer-headline .sub { display: block; font-size: 40px; margin-top: 4px; }

  .brand-mark {
    position: absolute; left: 37px; top: 200px; width: 237px; height: 150px;
    display: flex; flex-direction: column; align-items: center; justify-content: center; gap: 10px;
  }
  .brand-mark .dot {
    width: 70px; height: 70px; border-radius: 50%; background: var(--green-mid);
  }
  .brand-mark .name {
    font-family: var(--script); font-size: 28px; color: var(--green-mid);
  }
  .tagline {
    position: absolute; left: 0; width: 313px; top: 392px;
    text-align: center;
    font-family: var(--script); font-size: 20px; color: var(--green-mid);
  }

  .meadow-photo {
    position: absolute; left: 313px; top: 0; right: 0; bottom: 0;
    background:
      radial-gradient(circle at 85% 18%, rgba(255,250,200,0.95) 0, rgba(255,230,90,0.6) 14%, rgba(255,200,40,0) 34%),
      linear-gradient(180deg, #f5a21f 0%, #f7c531 20%, #eee25a 30%, #6f9b2a 34%, #a9d833 45%, #7fcb1f 70%, #5fb51b 100%);
  }

  .ribbon {
    position: absolute; left: 313px; height: 40px;
    background: var(--ribbon);
    border-radius: 0 6px 6px 0;
    font-family: var(--script); font-size: 22px; color: var(--white);
    display: flex; align-items: center; padding-left: 50px;
    text-shadow: 0 0 3px rgba(20,120,20,0.6);
  }
  .ribbon::before {
    content: ""; position: absolute; left: 0; top: 0; width: 38px; height: 100%;
    background: var(--white);
    clip-path: polygon(0 0, 100% 50%, 0 100%);
  }
  .ribbon--first { top: 127px; width: 597px; }
  .ribbon--second { top: 190px; width: 534px; }

  .promise {
    position: absolute; left: 358px; top: 250px;
    font-family: var(--sans); font-weight: 800; font-size: 31px; line-height: 1.2;
    color: var(--orange);
    text-shadow: -2px -2px 0 #fff, 2px -2px 0 #fff, -2px 2px 0 #fff, 2px 2px 0 #fff, 0 2px 0 #fff, 0 -2px 0 #fff;
  }

  .contact {
    position: absolute; right: 16px; top: 338px;
    text-align: right;
    font-family: var(--sans); font-weight: 700; font-size: 16px; line-height: 22px;
    color: var(--white);
    text-shadow: -1px -1px 0 var(--green-deep), 1px -1px 0 var(--green-deep), -1px 1px 0 var(--green-deep), 1px 1px 0 var(--green-deep);
  }

  /* ---------- Back ---------- */
  .field-photo {
    position: absolute; inset: 0;
    background: linear-gradient(180deg, #5fc3ee 0%, #bfe6f5 22%, #e8f4f4 36%, #6aa84a 41%, #3f9a34 46%, #7fd83a 55%, #4fc21e 80%, #2fae14 100%);
  }
  .services-intro {
    position: absolute; left: 15px; top: 10px;
    font-family: var(--script); font-size: 27px; line-height: 1.2;
    color: var(--white);
    text-shadow: -2px -2px 0 var(--green-deep), 2px -2px 0 var(--green-deep), -2px 2px 0 var(--green-deep), 2px 2px 0 var(--green-deep);
  }
  .back-contact {
    position: absolute; right: 15px; top: 14px; text-align: right;
  }
  .back-contact .business {
    font-family: var(--script); font-size: 38px; color: var(--green-deep); line-height: 1.1;
    text-shadow: -2px -2px 0 #fff, 2px -2px 0 #fff, -2px 2px 0 #fff, 2px 2px 0 #fff;
  }
  .back-contact .line {
    font-family: var(--sans); font-weight: 800; font-size: 26px; line-height: 1.4;
    color: var(--green-lime);
    text-shadow: -2px -2px 0 #fff, 2px -2px 0 #fff, -2px 2px 0 #fff, 2px 2px 0 #fff;
  }

  .signpost {
    position: absolute; top: 87px; bottom: 0; width: 22px;
    background: var(--post); opacity: 0.85;
  }
  .signpost--left { left: 113px; }
  .signpost--right { left: 335px; }

  .sign {
    position: absolute; height: 28px; width: 182px;
    display: flex; align-items: center; justify-content: center;
    font-family: var(--sans); font-weight: 700; font-size: 17px;
  }
  .sign--light { background: var(--green-light); color: var(--white); }
  .sign--dark { background: var(--green-mid); color: var(--yellow-text); }
  .sign--left { clip-path: polygon(12% 0, 100% 0, 100% 100%, 12% 100%, 0 50%); padding-left: 16px; }
  .sign--right { clip-path: polygon(0 0, 88% 0, 100% 50%, 88% 100%, 0 100%); padding-right: 16px; }
  .col-a { left: 26px; }
  .col-b { left: 246px; }
  .sign--small { font-size: 12px; }

  .closing {
    position: absolute; left: 442px; top: 336px;
    font-family: var(--script); font-size: 27px; line-height: 1.25;
    color: var(--white);
    text-shadow: 0 0 4px rgba(10,90,10,0.5);
  }
</style>
</head>
<body>

<section class="flyer flyer--front">
  <div class="meadow-photo" role="img" aria-label="Sunlit meadow of green grass and yellow wildflowers under an orange sunrise sky"></div>

  <div class="offer-panel">
    <h1 class="offer-headline"><span class="big">50% off</span><span class="sub">lawn mowing</span></h1>
    <div class="brand-mark">
      <span class="dot"></span>
      <span class="name">Kestrel Greens</span>
    </div>
    <p class="tagline">Lawn and Garden Maintenance</p>
  </div>

  <p class="ribbon ribbon--first">applies to first lawn mowed on any regular service</p>
  <p class="ribbon ribbon--second">applies to first 100 callers only, so call now!</p>

  <p class="promise">Professional lawn mowing<br>at an affordable price.</p>

  <address class="contact" style="font-style:normal">
    Tom and Gareth<br>
    Ph: 0487650912<br>
    Email: kestrelgreens@mailbox-example.com<br>
    www.kestrelgreens-example.com.au
  </address>
</section>

<section class="flyer flyer--back">
  <div class="field-photo" role="img" aria-label="Open green field with a tree line under a bright blue sky with clouds"></div>

  <h2 class="services-intro">At Kestrel Greens we specialise in<br>the following services;</h2>

  <div class="back-contact">
    <div class="business">Kestrel Greens</div>
    <div class="line">Ph 0487650912</div>
    <div class="line">www.kestrelgreens-example.com.au</div>
  </div>

  <div class="signpost signpost--left"></div>
  <div class="signpost signpost--right"></div>

  <ul class="services" style="list-style:none">
    <li class="sign sign--light sign--left col-a" style="top:126px">Lawn mowing</li>
    <li class="sign sign--dark sign--left col-a" style="top:165px">Edging</li>
    <li class="sign sign--light sign--left col-a" style="top:201px">Blowing</li>
    <li class="sign sign--dark sign--right col-a" style="top:238px">Hedging</li>
    <li class="sign sign--light sign--right col-a" style="top:273px">Pruning</li>
    <li class="sign sign--light sign--left col-a" style="top:305px">Tree Loping</li>
    <li class="sign sign--dark sign--left col-a" style="top:342px">Weeding</li>

    <li class="sign sign--dark sign--right col-b" style="top:126px">Poisoning</li>
    <li class="sign sign--light sign--left col-b" style="top:164px">Mulching</li>
    <li class="sign sign--dark sign--right col-b" style="top:202px">Fertilising</li>
    <li class="sign sign--light sign--left col-b" style="top:240px">Rubbish removal</li>
    <li class="sign sign--dark sign--right col-b" style="top:273px">Planting</li>
    <li class="sign sign--light sign--left col-b sign--small" style="top:306px">Lawn care and advice</li>
    <li class="sign sign--light sign--right col-b" style="top:342px">Turf</li>
  </ul>

  <p class="closing">And any other garden maintenance job,<br>No job too big or too small.</p>
</section>

</body>
</html>
```